Inspirational music needs a cd cover design

This CD is an individual project (no company). It is meant to reach
as many people as possible with great, inspiring music. It will be
available by mail and at gigs.

The cover will be a 4-panel eco-wallet (front cover, back cover, left
and right inside panels). I have a template from the CD manufacturing
company.

Target Market(s)

I am aiming for a very broad market. That said, the median age will
likely be 40 years old, and the CD will particularly appeal to people
concerned about climate change and activism, especially in the U.S.

Industry/Entity Type

It Company

Colors

Designer to choose colors to be used in the design.

Requirements
Must have
• I have an image that I would like on the front cover, and on the CD
• itself. It is a photo of a painting. I also have a photo of me for the back cover. For the background on the inner 2 panels I don't have an image but would like an image of a sky with storm clouds as long as the text is clearly readable.
• Typefaces: For the informational text I'd like something easy to read, like Verdana. For the album title and my name on the front cover, two typeface examples I like are the cover of Colin Ashbury Trio "Beside the Harbor and Drifting" and Gordon Velsky and Lanternfall "Hum Stone."

```html
<!DOCTYPE html>
<html lang="en">
<head>
<meta charset="utf-8">
<title>Wide Open Sky – Disc Label</title>
<link rel="stylesheet" href="https://fonts.googleapis.com/css2?family=Bitter:wght@700&family=Source+Sans+3:wght@400;500&display=swap">
<style>
  :root {
    --paper: #ffffff;
    --ink-light: #ffffff;
    --moss: #a9a32e;
    --sky-blue: #8fa6c4;
    --slate: #5d6a86;
    --violet: #4b3f6e;
    --rust: #9a5a35;
  }
  html, body {
    margin: 0;
    padding: 0;
    width: 1200px;
    height: 1200px;
    overflow: hidden;
    background: var(--paper);
  }
  .disc-canvas {
    position: relative;
    width: 1200px;
    height: 1200px;
  }
  .disc-art {
    position: absolute;
    inset: 0;
  }
  .title-arc,
  .artist-arc {
    font-family: "Bitter", Georgia, serif;
    font-weight: 700;
    fill: var(--ink-light);
    letter-spacing: 3px;
  }
  .title-arc { font-size: 74px; }
  .artist-arc { font-size: 70px; }
  .tracklist {
    position: absolute;
    margin: 0;
    padding: 0;
    list-style: none;
    font-family: "Source Sans 3", Verdana, sans-serif;
    font-size: 20px;
    line-height: 26.4px;
    color: var(--ink-light);
    text-shadow: 0 0 3px rgba(30, 35, 50, 0.55);
  }
  .tracklist li {
    display: flex;
    white-space: nowrap;
  }
  .tracklist .track-no {
    display: inline-block;
    width: 36px;
  }
  .tracklist--side-a {
    left: 462px;
    top: 300px;
  }
  .tracklist--side-b {
    left: 476px;
    top: 717px;
  }
</style>
</head>
<body>
<main class="disc-canvas">
  <svg class="disc-art" width="1200" height="1200" viewBox="0 0 1200 1200" xmlns="http://www.w3.org/2000/svg">
    <defs>
      <linearGradient id="painting-tones" x1="0" y1="0" x2="0.9" y2="1">
        <stop offset="0" stop-color="#b9b36a"/>
        <stop offset="0.3" stop-color="#a9a32e"/>
        <stop offset="0.5" stop-color="#8e97a8"/>
        <stop offset="0.7" stop-color="#8fa6c4"/>
        <stop offset="1" stop-color="#5d6a86"/>
      </linearGradient>
      <radialGradient id="painting-accent" cx="0.85" cy="0.35" r="0.3">
        <stop offset="0" stop-color="#9a5a35" stop-opacity="0.5"/>
        <stop offset="1" stop-color="#9a5a35" stop-opacity="0"/>
      </radialGradient>
      <path id="title-path" d="M 268 604 A 340 340 0 0 1 948 604"/>
      <path id="artist-path" d="M 232 604 A 376 376 0 0 0 984 604"/>
    </defs>

    <g role="img" aria-label="Painting of people gathered outdoors among trees and swirling blue water, in muted olive, blue and violet tones">
      <circle cx="608" cy="604" r="456" fill="url(#painting-tones)"/>
      <circle cx="608" cy="604" r="456" fill="url(#painting-accent)"/>
    </g>

    <circle class="disc-hole" cx="608" cy="604" r="86" fill="var(--paper)"/>

    <text class="title-arc">
      <textPath href="#title-path" startOffset="50%" text-anchor="middle">WIDE OPEN SKY</textPath>
    </text>
    <text class="artist-arc">
      <textPath href="#artist-path" startOffset="50%" text-anchor="middle">DANIEL ORRIN</textPath>
    </text>
  </svg>

  <ol class="tracklist tracklist--side-a">
    <li><span class="track-no">1.</span>The Ballad of Will Hadley</li>
    <li><span class="track-no">2.</span>Another World</li>
    <li><span class="track-no">3.</span>Ray’s Midnight Salvage Yard</li>
    <li><span class="track-no">4.</span>Beautiful</li>
    <li><span class="track-no">5.</span>The Quiet Millionaire</li>
    <li><span class="track-no">6.</span>Four Doors</li>
  </ol>

  <ol class="tracklist tracklist--side-b">
    <li><span class="track-no">7.</span>Long Ago Walkers</li>
    <li><span class="track-no">8.</span>Riverland</li>
    <li><span class="track-no">9.</span>Marisol’s Eyes</li>
    <li><span class="track-no">10.</span>Stand Up (featuring Rena Calloway)</li>
    <li><span class="track-no">11.</span>Will You Walk With Me</li>
  </ol>
</main>
</body>
</html>
```